依頼詳細
当会議が主催する講演会のチラシ製作をお願いいたします。
載せていただきたい事項は記載項目のとおりです。

【デザイン等について】
・昨年のチラシを添付しますので、参考にしてください。
・デザイン、レイアウト、色合いなどは全てお任せします
・昨年のデザインは堅苦しい印象がありましたので、今年はもう少し自由度のあるデザインを希望いたします。
・PRの強化に繋がるような、分かりやすく、且つ講演会に行きたくなる、目を引くようなデザインにしていただけたら幸いです。
・講師の写真を1枚載せてください(添付の写真データを使用願います)
・A4 縦 フルカラー
記載項目
キャッチコピー:地方の実情に合った新幹線の在り方について学ぼう

講演:「白峰新幹線実現の可能性を探る~在来線、ミニ新幹線からフル規格の新幹線へ~」

講師:鉄道ジャーナリスト 柴田 亮 氏

とき:平成28年7月5日(火) 午後3時~

ところ:桐ヶ丘グランドホテル
桐ヶ丘市松葉町二丁目3番4号

主催:北辰新幹線青葉延伸推進会議

お問い合わせ:北辰新幹線青葉延伸推進会議事務局(桐ヶ丘市役所企画課内)
Tel 0199-42-8670

※「申込不要・入場無料」の文言を入れてください。
サイズ
A4
ページ数
片面
希望イメージ
シンプル 複雑
単色 カラフル
暗い 明るい
日常 高級
遊び心 厳粛
未来的 伝統的
女性的 男性的
希望する色
納品ファイル
• イラストレーター形式 (.ai)
補足説明
※イラストレーターファイルはアウトライン必須、カラーモードはCMYKで納品願います。
※PDF形式も納品願います。
※納品は電子メール形式でお願いします。
※提案いただいたデザインの中から必ずコンペの当選者を選定します。(内容によっては修正をお願いする場合があります)
※ 募集期間を6月15日(水)としておりましたが、提案件数が希望数に達したため、誠に勝手ながら、6月14日(火)の正午をもって締め切りとさせていただく予定ですのでご了承ください。

明るく、非常に分かりやすいデザインであり、やわらかくかつポップなデザインが気に入りました。

この度は素敵なデザインを提案していただき誠にありがとうございました。
クラウドソーシングのサービスを今回初めて利用させていただきましたが、スピーディーでかつ素晴らしいデザインを提案いただき正直驚きました。想像していた以上のデザインで非常にうれしく思っております。今後ともどうか一つよろしくお願いいたします。

```html
<!DOCTYPE html>
<html lang="ja">
<head>
<meta charset="utf-8">
<title>白峰新幹線 講演会</title>
<link rel="stylesheet" href="https://fonts.googleapis.com/css2?family=Noto+Sans+JP:wght@400;500;700;900&family=Noto+Serif+JP:wght@500;700&display=swap">
<style>
  :root{
    --red:#d7191c;
    --navy:#13316e;
    --blue:#1d64b4;
    --sky:#e6f0fa;
    --ink:#222;
    --white:#fff;
  }
  *{margin:0;padding:0;box-sizing:border-box}
  html,body{width:846px;height:1200px;overflow:hidden;background:#fff}
  body{font-family:"Noto Sans JP",sans-serif;color:var(--ink)}
  .flyer{position:relative;width:846px;height:1200px;overflow:hidden;background:var(--white)}

  .hero-photo{position:absolute;left:0;top:0;width:846px;height:360px;
    background:linear-gradient(180deg,#5d6f86 0%,#8b9bb0 45%,#c9d3de 75%,#fff 100%)}

  .entry-badge{position:absolute;left:16px;top:68px;width:142px;height:118px;border-radius:14px;
    background:var(--red);color:var(--white);text-align:center;padding-top:20px;
    box-shadow:0 3px 8px rgba(0,0,0,.25)}
  .entry-badge .free{font-size:34px;font-weight:900;letter-spacing:1px;line-height:1.1}
  .entry-badge .no-apply{font-size:18px;font-weight:700;margin-top:8px}

  .catch{position:absolute;left:282px;top:96px;width:212px;height:136px;
    background:rgba(255,255,255,.55);display:flex;justify-content:center;align-items:flex-start;padding-top:10px}
  .catch p{writing-mode:vertical-rl;font-family:"Noto Serif JP",serif;font-weight:500;font-size:20px;
    line-height:1.7;color:var(--navy);letter-spacing:2px}

  .title{position:absolute;left:70px;top:318px;color:var(--red);font-weight:900;white-space:nowrap;
    text-shadow:0 0 6px #fff,0 0 10px #fff}
  .title .lead{font-size:128px;letter-spacing:4px}
  .title .rest{font-size:84px;letter-spacing:2px}
  .subject{position:absolute;left:78px;top:448px;font-size:66px;font-weight:900;color:var(--navy);white-space:nowrap}
  .subject small{font-size:46px}
  .subtitle{position:absolute;left:0;width:846px;top:546px;text-align:center;font-size:27px;font-weight:700;color:var(--blue)}

  .label{position:absolute;width:64px;height:64px;border-radius:50%;background:var(--blue);color:var(--white);
    font-size:20px;font-weight:700;display:flex;align-items:center;justify-content:center}
  .date-era{position:absolute;left:104px;top:604px;font-size:30px;font-weight:900;color:var(--navy)}
  .date-day{position:absolute;left:100px;top:620px;font-size:104px;font-weight:900;color:var(--navy);white-space:nowrap;letter-spacing:-2px}
  .date-day span{font-size:64px}
  .weekday{position:absolute;left:430px;top:668px;width:54px;height:54px;border-radius:50%;background:var(--red);
    color:var(--white);font-size:30px;font-weight:900;display:flex;align-items:center;justify-content:center}
  .date-time{position:absolute;left:104px;top:734px;font-size:46px;font-weight:900;color:var(--navy)}

  .venue{position:absolute;left:104px;top:798px;font-size:33px;font-weight:900;color:var(--navy);white-space:nowrap}
  .address{position:absolute;left:106px;top:844px;font-size:18px;font-weight:500;color:var(--ink)}

  .contact{position:absolute;left:26px;top:884px;width:468px;height:130px;border:3px solid var(--blue);border-radius:12px;
    background:var(--white);padding:12px 16px}
  .contact h3{font-size:19px;font-weight:700;color:var(--navy)}
  .contact .office{font-size:17px;font-weight:700;color:var(--navy);margin-top:2px}
  .contact .office small{font-size:12px;font-weight:500}
  .contact .tel{display:flex;align-items:center;gap:8px;margin-top:4px;font-size:46px;font-weight:900;color:var(--blue);line-height:1}

  .speaker-photo{position:absolute;left:512px;top:600px;width:334px;height:470px;
    background:linear-gradient(180deg,#dce6f1 0%,#b9c6d6 55%,#3a4150 100%)}
  .speaker-band{position:absolute;left:470px;top:1050px;width:376px;height:80px;background:var(--white)}
  .speaker-band .role{position:absolute;left:90px;top:6px;background:var(--blue);color:var(--white);font-size:17px;font-weight:700;padding:2px 10px}
  .speaker-band .kind{position:absolute;left:20px;top:24px}
  .speaker-band .name{position:absolute;left:90px;top:28px;font-size:44px;font-weight:900;color:var(--navy);white-space:nowrap;line-height:1.1}
  .speaker-band .name span{font-size:26px}

  .host{position:absolute;left:0;bottom:0;width:846px;height:62px;background:var(--sky);
    display:flex;align-items:center;justify-content:center;font-size:22px;font-weight:700;color:var(--navy)}
</style>
</head>
<body>
<main class="flyer">
  <div class="hero-photo" role="img" aria-label="白と赤の新幹線車両がホームに停車している写真"></div>

  <div class="entry-badge">
    <div class="free">入場無料</div>
    <div class="no-apply">(申込不要)</div>
  </div>

  <div class="catch"><p>地方の実情に合った<br>新幹線の在り方<br>について学ぼう</p></div>

  <h1 class="title"><span class="lead">白峰</span><span class="rest">新幹線</span></h1>
  <p class="subject">実現の<small>可能性</small>を探る</p>
  <p class="subtitle">～在来線、ミニ新幹線からフル規格の新幹線へ～</p>

  <div class="label" style="left:26px;top:640px">とき</div>
  <p class="date-era">平成28年</p>
  <p class="date-day">7<span>月</span>5<span>日</span></p>
  <div class="weekday">火</div>
  <p class="date-time">午後3時～</p>

  <div class="label" style="left:26px;top:800px;font-size:17px">ところ</div>
  <p class="venue">桐ヶ丘グランドホテル</p>
  <p class="address">桐ヶ丘市松葉町二丁目3番4号</p>

  <section class="contact">
    <h3>お問い合わせ</h3>
    <p class="office">北辰新幹線青葉延伸推進会議事務局<small>(桐ヶ丘市役所企画課内)</small></p>
    <p class="tel">
      <svg width="40" height="40" viewBox="0 0 24 24" aria-hidden="true"><path fill="#1d64b4" d="M6.6 10.8a15.1 15.1 0 0 0 6.6 6.6l2.2-2.2a1 1 0 0 1 1-.25 11.4 11.4 0 0 0 3.6.57 1 1 0 0 1 1 1V20a1 1 0 0 1-1 1A17 17 0 0 1 3 4a1 1 0 0 1 1-1h3.5a1 1 0 0 1 1 1c0 1.25.2 2.45.57 3.57a1 1 0 0 1-.25 1z"/></svg>
      0199-42-8670
    </p>
  </section>

  <div class="speaker-photo" role="img" aria-label="講師 柴田 亮 氏の上半身ポートレート写真"></div>
  <div class="speaker-band">
    <span class="label kind" style="width:54px;height:54px;font-size:16px;position:absolute">講師</span>
    <span class="role">鉄道ジャーナリスト</span>
    <p class="name">柴田 亮<span>氏</span></p>
  </div>

  <footer class="host">主催／北辰新幹線青葉延伸推進会議</footer>
</main>
</body>
</html>
```